Stationery Refresh For Local Mortgage Broker

We want to modernise and standardise our stationery, including: letterhead, presentation folder, email signature and business card.

The new stationery should be a more modern and professional take on our existing colour scheme and brand. (We do not want a complete overhaul.) A folder of approved stock photos can be found here: https://filebox.example-share.net/f/7kQzR2mTn4vWx9Lp3Yb8-HsdJe5Uc1Ga/view

Our current website is: www.brindlecovefin.com.au but we will be updating this to be consistent with our new stationery.

We are open to *very slight* tweaks to our logo if you feel it needs modernising, but overall we would like to maintain consistent colour scheme.

> Letterhead

148 Calloway Parade,
Harrowvale, VIC, 3281
ABN: 31 805 249 067
Australian Credit License: 718293

(03) 5391 6084
www.brindlecovefin.com.au

> Presentation Folder

148 Calloway Parade,
Harrowvale, VIC, 3281
(03) 5391 6084
www.brindlecovefin.com.au

ABN: 31 805 249 067

> Email Signature

Liam Tresidder
Director
M. 0412 857 294
P. (03) 5391 6084
www.brindlecovefin.com.au
148 Calloway Parade,
Harrowvale, VIC, 3281

ABN: 31 805 249 067

(you can also include a photo if you like: https://brindlecovefin.com.au/wp-content/uploads/2020/12/Liam-Tresidder.png.webp)

> Business Card

Liam Tresidder
Director
M. 0412 857 294
P. (03) 5391 6084
www.brindlecovefin.com.au
148 Calloway Parade,
Harrowvale, VIC, 3281

ABN: 31 805 249 067

Additional information...

If it's useful/relevant, the services we offer are: Home Loans, Investment Loans, Refinance, Debt Consolidation, Commercial Finance, Vehicle Loans
(You may choose to use this in any of the designs)

Target Market(s)

Home Buyers and Investors

Industry/Entity Type

Mortgage broking/property/real estate

Requirements
Must have
• At least somewhat consistent with our current site (yet meaningfully modernized)
Should not have
• dramatically different logo or colourscheme overhauls

```html
<!DOCTYPE html>
<html lang="en">
<head>
<meta charset="utf-8">
<title>Brindlecove Financial Services – Stationery</title>
<link href="https://fonts.googleapis.com/css2?family=Montserrat:wght@300;400;500;600&display=swap" rel="stylesheet">
<style>
:root{
  --board:#e1e1e1;
  --paper:#ffffff;
  --maroon:#5c0b0d;
  --maroon-deep:#580a0c;
  --maroon-inside:#6b1214;
  --brand-red:#8e1b1d;
  --brand-dark:#6b0f12;
  --ink:#6a6a6a;
  --label:#111111;
}
*{margin:0;padding:0;box-sizing:border-box}
html,body{width:1200px;height:853px;overflow:hidden;background:var(--board)}
body{position:relative;font-family:"Montserrat",Arial,sans-serif}
.sheet{position:absolute;background:var(--paper)}
.label{position:absolute;font-family:Arial,Helvetica,sans-serif;font-size:10px;color:var(--label);letter-spacing:.2px}
.wordmark{position:absolute;text-align:center;color:var(--brand-red);font-weight:400;white-space:nowrap;line-height:1}
.rule{position:absolute;top:0;bottom:0;width:2px;background:var(--brand-red)}
.small{position:absolute;font-size:4px;letter-spacing:1px;color:var(--ink);line-height:5.2px;white-space:nowrap}
.legal{position:absolute;font-family:Arial,Helvetica,sans-serif;font-size:4.2px;color:var(--ink);display:flex;align-items:center;gap:4px;white-space:nowrap}
.legal .sep{width:.5px;height:8px;background:var(--ink)}
.folder{position:absolute;width:259px;height:346px;background:var(--maroon)}
.folder.inside{background:var(--maroon-inside)}
.pocket{position:absolute;left:0;top:0}
</style>
</head>
<body>

<!-- Letterhead front -->
<section class="sheet letterhead-front" style="left:41px;top:53px;width:259px;height:346px">
  <div class="wordmark" style="left:8px;width:82px;top:24px;font-size:7.5px;letter-spacing:3px;padding-left:3px;color:var(--brand-dark)">BRINDLECOVE</div>
  <div class="small" style="left:8px;width:82px;top:50px;text-align:center;padding-left:1px">
    148 CALLOWAY PARADE<br>HARROWVALE | VIC - 3281<br>(03) 5391 6084<br>WWW.BRINDLECOVEFIN.COM.AU
  </div>
  <div class="legal" style="left:9px;top:335px">
    <span>ABN: 31 805 249 067</span><span class="sep"></span><span>AUSTRALIAN CREDIT LICENSE: 718293</span>
  </div>
  <div class="rule" style="left:237px;background:var(--brand-dark)"></div>
</section>
<div class="label" style="left:41px;top:404px">LETTERHEAD FRONT</div>

<!-- Letterhead back -->
<section class="sheet letterhead-back" style="left:328px;top:53px;width:259px;height:346px">
  <div class="wordmark" style="left:0;right:0;top:324px;font-size:8px;letter-spacing:3.4px;padding-left:3.4px;color:var(--brand-dark)">BRINDLECOVE</div>
</section>
<div class="label" style="left:328px;top:404px">LETTERHEAD BACK</div>

<!-- Business card front -->
<section class="sheet card-front" style="left:654px;top:58px;width:229px;height:130px">
  <div class="wordmark" style="left:0;width:210px;top:21px;font-size:6px;letter-spacing:2.6px;padding-left:2.6px">BRINDLECOVE</div>
  <div style="position:absolute;left:0;width:210px;top:58px;text-align:center">
    <div style="font-size:4px;font-weight:600;letter-spacing:1.2px;color:#555">LIAM TRESIDDER</div>
    <div style="font-size:3.6px;letter-spacing:1px;color:var(--ink);margin-top:1.5px">DIRECTOR</div>
  </div>
  <div class="small" style="left:0;width:210px;top:90px;text-align:center;font-size:3.6px">
    M.0412 857 294<br>P.(03) 5391 6084<br>WWW.BRINDLECOVEFIN.COM.AU<br>148 CALLOWAY PARADE<br>HARROWVALE | VIC - 3281
  </div>
  <div class="legal" style="left:0;width:210px;top:120px;justify-content:center;font-size:2.2px;gap:3px">
    <span>ABN: 31 805 249 067</span><span class="sep" style="height:5px"></span><span>AUSTRALIAN CREDIT LICENSE: 718293</span>
  </div>
  <div class="rule" style="left:210px"></div>
</section>
<div class="label" style="left:655px;top:193px">BUSINESS CARD FRONT</div>

<!-- Business card back -->
<section class="sheet card-back" style="left:904px;top:58px;width:229px;height:130px">
  <div class="wordmark" style="left:0;right:0;top:62px;font-size:10px;letter-spacing:4.6px;padding-left:4.6px">BRINDLECOVE</div>
</section>
<div class="label" style="left:904px;top:193px">BUSINESS CARD BACK</div>

<!-- Email signature -->
<section class="sheet email-signature" style="left:654px;top:279px;width:170px;height:88px">
  <div class="wordmark" style="left:6px;width:56px;top:41px;font-size:5px;letter-spacing:1.8px;padding-left:1.8px">BRINDLECOVE</div>
  <div class="small" style="left:72px;top:19px;font-size:3.7px;line-height:5.9px">
    LIAM TRESIDDER<br>DIRECTOR<br>M.0412 857 294<br>P.(03) 5391 6084<br>WWW.BRINDLECOVEFIN.COM.AU<br>148 CALLOWAY PARADE<br>HARROWVALE | VIC - 3281
  </div>
  <div class="legal" style="left:72px;top:63px;font-size:2px;gap:3px">
    <span>ABN: 31 805 249 067</span><span class="sep" style="height:4px"></span><span>AUSTRALIAN CREDIT LICENSE: 718293</span>
  </div>
</section>
<div class="label" style="left:656px;top:372px">EMAIL SIGNATURE</div>

<!-- Folder outside front -->
<section class="folder outside-front" style="left:41px;top:442px">
  <div class="wordmark" style="left:134px;width:98px;top:172px;font-size:9px;letter-spacing:4.4px;padding-left:4.4px;color:#fff">BRINDLECOVE</div>
  <div style="position:absolute;left:235px;top:0;bottom:0;width:2px;background:var(--paper)"></div>
</section>
<div class="label" style="left:41px;top:794px">FOLDER - OUTSIDE FRONT</div>

<!-- Folder outside back -->
<section class="folder outside-back" style="left:328px;top:442px">
  <div class="wordmark" style="left:0;right:0;top:299px;font-size:8px;letter-spacing:3.4px;padding-left:3.4px;color:#fff">BRINDLECOVE</div>
  <div class="legal" style="left:0;right:0;top:331px;justify-content:center;color:#fff;font-size:4px">
    <span>ABN: 31 805 249 067</span><span class="sep" style="background:#fff"></span><span>AUSTRALIAN CREDIT LICENSE: 718293</span>
  </div>
</section>
<div class="label" style="left:328px;top:794px">FOLDER - OUTSIDE BACK</div>

<!-- Folder inside front -->
<section class="folder inside inside-front" style="left:618px;top:442px">
  <svg class="pocket" width="259" height="346" viewBox="0 0 259 346"><polygon points="0,223 245,223 259,346 0,346" fill="var(--maroon-deep)"/></svg>
  <div class="small" style="left:13px;top:304px;color:#fff;font-size:4.2px;line-height:6.5px">
    148 CALLOWAY PARADE<br>HARROWVALE | VIC - 3281<br>(03) 5391 6084<br>WWW.BRINDLECOVEFIN.COM.AU
  </div>
</section>
<div class="label" style="left:617px;top:794px">FOLDER - INSIDE FRONT</div>

<!-- Folder inside back -->
<section class="folder inside inside-back" style="left:905px;top:442px">
  <svg class="pocket" width="259" height="346" viewBox="0 0 259 346"><polygon points="14,223 259,223 259,346 0,346" fill="var(--maroon-deep)"/></svg>
</section>
<div class="label" style="left:904px;top:794px">FOLDER - INSIDE BACK</div>

</body>
</html>
```